Pebblo Bites - Product Packaging (Snack wrapper)

Pebblo Bites is looking for our next package design! Our snack products are all-natural, gluten-free, vegan, and paleo. Our mission is to bring clean, wholesome snacks back into the market. The package design is for our individual wrappers that hold two of our snack bites.

The background will be matte white with a transparent window integrated so that customers can see the bites inside.

The final design will be clean and modern, using white as the background, black for text, and our logos yellow. We have multiple different flavors, so each flavor will have its own unique color accents that must be editable in the final file. The accent colors should be bold and take up an equal amount of space as the white does.

The packaging will stand out on a busy shelf and entice customers as an easy on-the-go, wholesome snack. The back of the package must have a space for a nutrition box and ingredients list. Our logo is attached. The logo graphic can be separated (it doesnt have to stay in the same layout you see). We have attached an example of our old product label, too.

The package dimensions are 4inches wide x 5 inches long with a 1/2inch of the length at the top and 1/2inch of the length at the bottom being blank for sealing. Thank you!

Target Market(s)

Cafe goers, health-conscience, kids, active.

Font styles to use
Sans Serif

Colors
fbed22
ffffff
000000

Requirements
Must have
• Must show that our product is gluten-free, vegan, and paleo. Must have editable flavor name, and flavor accent colors for our multiple different flavors. Must use our logo and company yellow.

```html
<!DOCTYPE html>
<html lang="en">
<head>
<meta charset="utf-8">
<title>Pebblo Bites – Snack Wrappers</title>
<link rel="stylesheet" href="https://fonts.googleapis.com/css2?family=Montserrat:wght@400;600&family=Roboto+Condensed:wght@700&display=swap">
<style>
  :root {
    --backdrop: #dfe2e5;
    --wrapper-white: #ffffff;
    --seal: #eff0f2;
    --brand-yellow: #f2d51a;
    --accent-chocolate: #8cc4e8;
    --accent-bearclaw: #1ea94f;
    --band-text: #ffffff;
    --bite-light: #d9ab6b;
    --bite-mid: #c18d51;
    --bite-dark: #7a4a26;
  }
  * { box-sizing: border-box; margin: 0; padding: 0; }
  html, body { width: 1200px; height: 1200px; overflow: hidden; }
  body {
    background: var(--backdrop);
    font-family: "Montserrat", Arial, sans-serif;
    position: relative;
  }
  .wrapper {
    position: absolute;
    top: 340px;
    width: 420px;
    height: 560px;
    background: var(--wrapper-white);
    box-shadow: 0 6px 24px rgba(0,0,0,0.08);
  }
  .wrapper--chocolate-chip { left: 138px; --accent: var(--accent-chocolate); }
  .wrapper--bear-claw { left: 698px; --accent: var(--accent-bearclaw); }

  .seal { position: absolute; left: 0; width: 100%; height: 20px; background: var(--seal); }
  .seal--top { top: 0; }
  .seal--bottom { bottom: 0; }

  .brand-dot {
    position: absolute;
    top: 59px; left: 165px;
    width: 90px; height: 90px;
    border-radius: 50%;
    background: var(--accent);
  }
  .brand-name {
    position: absolute;
    top: 158px; left: 0; width: 100%;
    text-align: center;
    font-weight: 600;
    font-size: 64px;
    line-height: 76px;
    color: var(--brand-yellow);
  }
  .product-line {
    position: absolute;
    top: 240px; left: 0; width: 100%;
    text-align: center;
    font-size: 20px;
    line-height: 24px;
    color: var(--brand-yellow);
  }
  .flavor-band {
    position: absolute;
    top: 276px; left: 30px; right: 20px;
    height: 64px;
    background: var(--accent);
    display: flex; align-items: center; justify-content: center;
    font-family: "Roboto Condensed", "Arial Narrow", sans-serif;
    font-weight: 700;
    font-size: 38px;
    letter-spacing: 0.5px;
    color: var(--band-text);
    white-space: nowrap;
  }
  .claims {
    position: absolute;
    top: 345px; left: 5px; width: 100%;
    text-align: center;
    font-size: 19px;
    line-height: 24px;
    color: var(--brand-yellow);
    white-space: nowrap;
  }
  .window {
    position: absolute;
    top: 380px; left: 73px;
    width: 277px; height: 158px;
    background: radial-gradient(circle at 60% 45%, var(--bite-light) 0%, var(--bite-mid) 55%, var(--bite-dark) 100%);
  }
</style>
</head>
<body>
  <section class="wrapper wrapper--chocolate-chip">
    <div class="seal seal--top"></div>
    <div class="brand-dot"></div>
    <div class="brand-name">Pebblo</div>
    <div class="product-line">Cookie Bites</div>
    <div class="flavor-band">CHOCOLATE CHIP</div>
    <div class="claims">Gluten Free | Vegan | Paleo</div>
    <div class="window" role="img" aria-label="Close-up photo of chocolate chip cookie bites"></div>
    <div class="seal seal--bottom"></div>
  </section>

  <section class="wrapper wrapper--bear-claw">
    <div class="seal seal--top"></div>
    <div class="brand-dot"></div>
    <div class="brand-name">Pebblo</div>
    <div class="product-line">Cookie Bites</div>
    <div class="flavor-band">BEAR CLAW</div>
    <div class="claims">Gluten Free | Vegan | Paleo</div>
    <div class="window" role="img" aria-label="Close-up photo of cookie bites"></div>
    <div class="seal seal--bottom"></div>
  </section>
</body>
</html>
```